We are launching a new supplement that helps you lose weight.

We are looking for a logo and some ideas around an A4 advert. We are not looking for a finished product as we can do that in house with our internal design team.

With pixel harbor, we always offer a first second and third prize and then once we pay out, we then use the supplied files to finish the project in house. We normally take components from the top three concepts.

Fenro BLITZ

Contains glucomannan extracts from the Konjak plant (which we nicknamed Velta-R) has been clinically proven to aid weight loss. So much so, that it is the only ingredient in the world that has been approved by the Varden Authority to help us lose weight.

How Fenro BLITZ work..
Velta-R is a natural plant fibre, which as well as being beneficial for our gut, also expands and makes us feel fuller for longer. In the stomach it acts a bit like a sponge and as it absorbs water safely expands. Taken before a meal it reduces our appetite, so we eat smaller portions and can even completely remove the desire to eat snacks.

The science bit
When taken before a meal, Fenro BLITZ reduces the hormone that tells the brain that we are hungry (leptin) and increases the hormone that sends the signal to the brain to stop eating (ghrelin

Target Market(s)

Male and female, from 30 years plus

Industry/Entity Type

Weight

Requirements
Must have
• Concept and layout for an A4 advert to go into health magazines and female titles. Copy heavy advert, Similar to old style direct-mail.
• Can you try to use pictovale 842193056 or something similar
Nice to have
• Fonts and imagery. I have a few images attached, one is the logo, and to our other products from a range of supplements.

```html
<!DOCTYPE html>
<html lang="en">
<head>
<meta charset="utf-8">
<title>Fenro BLITZ Velta-R advert</title>
<link rel="stylesheet" href="https://fonts.googleapis.com/css2?family=Oswald:wght@500;700&family=Roboto+Condensed:wght@400;700&display=swap">
<style>
  :root {
    --ink: #0d0d0f;
    --panel: #141416;
    --red: #d0151d;
    --red-deep: #8e0b10;
    --white: #ffffff;
    --body-text: #e6e6e6;
    --photo-warm: #7a5a48;
    --photo-dark: #2a1c18;
  }
  * { margin: 0; padding: 0; box-sizing: border-box; }
  html, body { width: 933px; height: 1200px; overflow: hidden; background: var(--ink); }
  .advert {
    position: relative;
    width: 933px;
    height: 1200px;
    overflow: hidden;
    background: radial-gradient(circle at 300px 330px, rgba(160,15,20,0.55), transparent 300px), var(--ink);
    font-family: "Roboto Condensed", sans-serif;
    color: var(--white);
  }
  .shapes { position: absolute; inset: 0; }
  .brand {
    position: absolute;
    left: 120px;
    top: 40px;
    width: 360px;
    text-align: center;
    font-family: "Oswald", sans-serif;
    font-weight: 700;
    color: var(--white);
  }
  .brand-name { font-size: 76px; line-height: 1; letter-spacing: 1px; }
  .brand-variant {
    display: inline-block;
    margin-top: 12px;
    padding: 4px 26px;
    background: var(--red);
    font-size: 34px;
    line-height: 1.1;
  }
  .headline {
    position: absolute;
    right: 16px;
    top: 28px;
    text-align: right;
    font-family: "Oswald", sans-serif;
  }
  .headline-main {
    color: var(--red);
    font-weight: 700;
    font-size: 104px;
    line-height: 0.98;
    text-transform: uppercase;
  }
  .headline-sub {
    margin-top: 10px;
    font-weight: 500;
    font-size: 24px;
    text-transform: uppercase;
    color: var(--white);
  }
  .copy {
    position: absolute;
    left: 509px;
    top: 838px;
    width: 398px;
    font-size: 11.2px;
    line-height: 1.32;
    color: var(--body-text);
  }
  .copy h2 {
    font-size: 13px;
    font-weight: 700;
    color: var(--red);
    margin-bottom: 8px;
  }
  .copy p { margin-bottom: 12px; }
  .copy p.spaced { margin-bottom: 22px; }
  .copy h2.later { margin-top: 0; margin-bottom: 10px; }
</style>
</head>
<body>
<main class="advert">
  <svg class="shapes" width="933" height="1200" viewBox="0 0 933 1200" aria-hidden="false">
    <defs>
      <linearGradient id="photoTone" x1="0" y1="0" x2="1" y2="1">
        <stop offset="0" stop-color="#a07a62"/>
        <stop offset="0.5" stop-color="var(--photo-warm)"/>
        <stop offset="1" stop-color="#d8c08a"/>
      </linearGradient>
      <linearGradient id="jarTone" x1="0" y1="0" x2="0" y2="1">
        <stop offset="0" stop-color="#c8141b"/>
        <stop offset="0.25" stop-color="#1a1a1c"/>
        <stop offset="1" stop-color="#0a0a0b"/>
      </linearGradient>
    </defs>
    <polygon points="12,11 83,49 12,87" fill="var(--red)"/>
    <rect class="photo" x="0" y="330" width="933" height="580" fill="url(#photoTone)" role="img" aria-label="Photo of five smiling friends at a bar raising blue shot glasses in a toast"/>
    <polygon points="0,795 440,880 0,1050" fill="var(--red)"/>
    <polygon points="0,1050 440,880 440,1200 0,1200" fill="var(--ink)"/>
    <polygon points="933,660 420,885 420,1200 933,1200" fill="var(--panel)"/>
    <line x1="933" y1="672" x2="440" y2="888" stroke="#555" stroke-width="1" stroke-dasharray="3 3"/>
    <polygon points="426,805 484,838 426,874" fill="var(--red)"/>
    <polygon points="751,599 827,637 751,686" fill="var(--red)"/>
    <polygon points="827,637 933,594 933,736" fill="var(--red)"/>
    <rect class="product-shot" x="40" y="760" width="390" height="420" rx="24" fill="url(#jarTone)" role="img" aria-label="Product shot of two Fenro BLITZ Velta-R supplement jars, large and small"/>
  </svg>

  <div class="brand">
    <div class="brand-name">FENRO BLITZ</div>
    <div class="brand-variant">VELTA-R</div>
  </div>

  <div class="headline">
    <div class="headline-main">Loss<br>Weight</div>
    <div class="headline-sub">Without changing your lifestyle!</div>
  </div>

  <section class="copy">
    <h2>Lorem Ipsum Dummy Text</h2>
    <p>Contains glucomannan extracts from the Konjak plant (which we nicknamed Velta-R) has been clinically proven to aid weight loss. So much so, that it is the only ingredient in the world that has been approved by the Varden Authority to help us lose weight. Contains glucomannan extracts from the Konjak plant (which we nicknamed Velta-R) has been clinically proven to aid weight loss. So much so, that it is the only ingredient in the world that has been approved by the Varden Authority to help us lose weight.</p>
    <p class="spaced">Contains glucomannan extracts from the Konjak plant (which we nicknamed Velta-R) has been clinically proven to aid weight loss. So much so, that it is the only ingredient in the world that has been approved by the Varden Authority to help us lose weight.</p>
    <p>Contains glucomannan extracts from the Konjak plant (which we nicknamed Velta-R) has been clinically proven to aid weight loss. So much so, that it is the only ingredient in the world that has been approved by the Varden Authority to help us lose weight.</p>
    <h2 class="later">How Fenro BLITZ work..</h2>
    <p>Velta-R is a natural plant fibre, which as well as being beneficial for our gut, also expands and makes us feel fuller for longer. In the stomach it acts a bit like a sponge and as it absorbs water safely expands. Taken before a meal it reduces our appetite, so we eat smaller portions and can even completely remove the desire to eat snacks.</p>
  </section>
</main>
</body>
</html>
```